V9 Web Design Project

New company website for Intel cyber security company.

Style should be cool, but remain appropriate for very serious subject matter and audience.

Target Market(s)

Target audience is government and the military

Navigation needs to include:
- About Us
- Services
- Careers
- Contact Us
- Contracts

As well as 2 feature areas - use "Technology Integration" and "Case Study" as the supporting headlines.

Industry/Entity Type

Security

Font styles to use
Sans Serif

Colors

Designer to choose colors to be used in the design.

Requirements
Must have
• Mountain imagery and theme.

Use logo attached.

New Tagline - "Securing the Continuum"
Nice to have
• Supporting imagery could include photos representative of security - avoid cliches.
Should not have
• Needs to be serious not frivolous

```html
<!DOCTYPE html>
<html lang="en">
<head>
<meta charset="utf-8">
<title>V9 Group — Securing the Continuum</title>
<link rel="stylesheet" href="https://fonts.googleapis.com/css2?family=Open+Sans:ital,wght@0,400;0,600;0,700;0,800;1,700&display=swap">
<style>
:root{
  --navy:#13244a;
  --navy-deep:#0d1a36;
  --blue:#24488e;
  --red:#b8312b;
  --ink:#2a2f3a;
  --muted:#6b7280;
  --line:#d7dbe2;
  --white:#ffffff;
  --footer:#1b1f27;
}
*{box-sizing:border-box;margin:0;padding:0}
html,body{width:1200px;height:2164px;overflow:hidden}
body{font-family:"Open Sans",Arial,sans-serif;color:var(--ink);background:var(--white);position:relative}
a{color:inherit;text-decoration:none}

.topbar{height:32px;background:var(--navy-deep);color:#c9d1e2;font-size:12px;display:flex;align-items:center;gap:28px;padding-left:120px}
.header{height:88px;display:flex;align-items:center;justify-content:space-between;padding:0 120px;background:var(--white)}
.brand{display:flex;align-items:center;gap:12px;font-weight:800;font-size:30px;color:var(--navy);letter-spacing:1px}
.brand-mark{width:34px;height:34px;background:var(--navy)}
.nav{display:flex;gap:4px;font-size:14px;font-weight:600}
.nav a{padding:10px 14px;color:var(--navy)}
.nav a.is-active{background:var(--navy);color:var(--white)}

.hero{position:relative;height:600px;background:linear-gradient(180deg,#8fb0d8 0%,#d9b59a 38%,#5b6f90 62%,#27324a 100%)}
.hero-title{position:absolute;top:250px;width:100%;text-align:center;color:var(--white);font-size:56px;font-weight:700;font-style:italic;text-shadow:0 2px 8px rgba(0,0,0,.45)}
.hero-btn{position:absolute;top:340px;left:548px;width:104px;height:38px;background:var(--navy);color:var(--white);font-size:14px;font-weight:600;display:flex;align-items:center;justify-content:center;border-radius:3px}

.features{position:absolute;top:680px;left:0;width:1200px;height:352px;display:flex}
.feature{color:var(--white);padding:64px 0 0 130px}
.feature-tech{width:672px;background:var(--blue);clip-path:polygon(0 30px,100% 0,100% 100%,0 100%)}
.feature-case{width:528px;background:var(--navy);padding:44px 90px 0 40px}
.feature h2{font-size:30px;font-weight:700;margin-bottom:18px}
.feature-list{list-style:none;font-size:14px;line-height:1.35}
.feature-list li{display:flex;gap:10px;margin-bottom:14px}
.feature-list svg{flex:none;margin-top:3px}
.btn-outline{display:inline-block;border:2px solid var(--white);padding:6px 14px;font-size:13px;font-weight:700;margin-top:10px}
.case-sub{font-weight:700;font-size:15px;color:#9fc0ff;margin:4px 0 10px}
.case-lead{font-weight:700;font-size:13px;margin-bottom:10px}
.case-body{font-size:13px;line-height:1.5;color:#d7def0;margin-bottom:14px}
.btn-solid{display:inline-block;background:var(--blue);padding:7px 14px;font-size:13px;font-weight:700}

.slider-arrows{position:absolute;top:1030px;left:1010px;display:flex;gap:6px}
.slider-arrows span{width:30px;height:30px;background:var(--navy);display:flex;align-items:center;justify-content:center}

.section-title{position:absolute;left:120px;width:960px;display:flex;align-items:center;gap:22px;color:var(--red);font-weight:700;font-size:30px;letter-spacing:1px;justify-content:center}
.section-title::before,.section-title::after{content:"";height:1px;background:var(--line);flex:1}
.welcome-title{top:1052px}
.service-title{top:1332px}

.intel{position:absolute;top:1112px;left:120px;width:960px;display:flex;gap:40px}
.intel-text{width:560px}
.intel-text h3{font-size:17px;font-weight:700;color:var(--navy);margin-bottom:10px}
.intel-text p{font-size:13px;line-height:1.6;color:var(--muted);margin-bottom:10px}
.intel-media{width:380px;height:208px;background:linear-gradient(135deg,#2d3b55,#7d8ca8 60%,#b9c3d6)}

.services{position:absolute;top:1392px;left:120px;width:960px;display:flex;justify-content:space-between}
.card{width:304px}
.card-media{height:148px;border-radius:2px}
.card-media.m1{background:linear-gradient(135deg,#0c2f6a,#2a6bc4)}
.card-media.m2{background:linear-gradient(135deg,#5a0f12,#c43a2f)}
.card-media.m3{background:linear-gradient(135deg,#0a1530,#253b73)}
.card h4{margin-top:18px;font-size:17px;font-weight:700;color:var(--navy)}
.card p{font-size:13px;line-height:1.5;color:var(--muted);margin:8px 0 10px}
.card .more{font-size:13px;font-weight:700;color:var(--navy)}

.testimonial{position:absolute;top:1680px;left:0;width:1200px;height:280px;background:linear-gradient(100deg,#1a2234 0%,#35415a 45%,#7c2a2e 80%,#2a3550 100%);color:var(--white);text-align:center}
.quote-mark{position:absolute;top:22px;left:582px}
.quote{position:absolute;top:58px;left:340px;width:520px;font-size:14px;line-height:1.55;font-style:italic}
.avatar{position:absolute;top:150px;left:570px;width:60px;height:60px;border-radius:50%;background:#c7b8a6;border:3px solid var(--white)}
.person{position:absolute;top:218px;width:100%;font-size:14px;font-weight:700}
.person small{display:block;font-weight:400;font-size:12px;color:#cfd6e4}

.partners{position:absolute;top:1990px;left:120px;width:960px;height:100px;display:flex;justify-content:space-between;align-items:center}
.partner{display:flex;align-items:center;gap:8px;font-size:22px;font-weight:700;color:var(--navy)}
.partner i{width:14px;height:14px;border-radius:50%;background:var(--red)}

.footer{position:absolute;bottom:0;left:0;width:1200px;height:56px;background:var(--footer);color:#b6bcc8;font-size:12px;display:flex;align-items:center;justify-content:space-between;padding:0 120px}
</style>
</head>
<body>

<div class="topbar">
  <span>1674 N Pine Street, Denver CO 80110</span>
  <span>+1 (303) 555-0148</span>
  <span>info@v9group.com</span>
</div>

<header class="header">
  <div class="brand"><span class="brand-mark"></span>V9 GROUP</div>
  <nav class="nav">
    <a href="#" class="is-active">Home</a>
    <a href="#">About Us</a>
    <a href="#">Services</a>
    <a href="#">Careers</a>
    <a href="#">Contract Us</a>
    <a href="#">Contacts</a>
  </nav>
</header>

<section class="hero" role="img" aria-label="Snow-capped mountain peak at sunrise">
  <h1 class="hero-title">Securing the Continuum</h1>
  <a href="#" class="hero-btn">Learn More</a>
</section>

<section class="features">
  <div class="feature feature-tech">
    <h2>Technology Integration</h2>
    <ul class="feature-list">
      <li><svg width="10" height="10"><rect width="10" height="10" fill="#fff"/></svg>One of the most comprehensive security portfolios around.</li>
      <li><svg width="10" height="10"><rect width="10" height="10" fill="#fff"/></svg>A real integration story.</li>
      <li><svg width="10" height="10"><rect width="10" height="10" fill="#fff"/></svg>A well established partner ecosystem.</li>
      <li><svg width="10" height="10"><rect width="10" height="10" fill="#fff"/></svg>A rich and popular monitor.</li>
    </ul>
    <a href="#" class="btn-outline">LEARN MORE</a>
  </div>
  <div class="feature feature-case">
    <h2>Case Study</h2>
    <div class="case-sub">Packline - USA Case Study Report</div>
    <div class="case-lead">Supplement to the 2013/2 Coastal Cyber Threat Index: USA Case Study Report.</div>
    <p class="case-body">The 2013/2 Coastal Cyber Threat Index is a strategic public-private partnership research project to support initiatives that seek to address the growing cyber threat facing the country.</p>
    <a href="#" class="btn-solid">READ MORE</a>
  </div>
</section>

<div class="slider-arrows">
  <span><svg width="10" height="12"><path d="M8 1 2 6l6 5" stroke="#fff" stroke-width="2" fill="none"/></svg></span>
  <span><svg width="10" height="12"><path d="M2 1l6 5-6 5" stroke="#fff" stroke-width="2" fill="none"/></svg></span>
</div>

<h2 class="section-title welcome-title">WELCOME TO V9 GROUP</h2>

<section class="intel">
  <div class="intel-text">
    <h3>INTEL CYBER SECURITY SYSTEMS INFORMATION</h3>
    <p>Contrary to popular belief, our work is not simply routine. It has roots in a piece of classical field research from many years ago, and a team that reviewed every detail, checking and testing each source across the whole network to find the places where risk truly begins.</p>
    <p>We go through the cites of the words in classical literature, discover the undoubtable source and trace each thread back to where it started. Every finding is checked twice before it reaches the people who rely on it.</p>
  </div>
  <div class="intel-media" role="img" aria-label="Hands typing on a laptop keyboard"></div>
</section>

<h2 class="section-title service-title">SERVICE</h2>

<section class="services">
  <article class="card">
    <div class="card-media m1" role="img" aria-label="Blue digital network graphic"></div>
    <h4>MANAGED SECURITY</h4>
    <p>Round the clock watch over your systems, with alerts handled by cleared analysts.</p>
    <a href="#" class="more">more »</a>
  </article>
  <article class="card">
    <div class="card-media m2" role="img" aria-label="Red padlock on circuit board"></div>
    <h4>MANAGED SECURITY</h4>
    <p>Round the clock watch over your systems, with alerts handled by cleared analysts.</p>
    <a href="#" class="more">more »</a>
  </article>
  <article class="card">
    <div class="card-media m3" role="img" aria-label="Dark blue shield and data screen"></div>
    <h4>MANAGED SECURITY</h4>
    <p>Round the clock watch over your systems, with alerts handled by cleared analysts.</p>
    <a href="#" class="more">more »</a>
  </article>
</section>

<section class="testimonial" role="img" aria-label="Waving national flag in background">
  <svg class="quote-mark" width="36" height="28" viewBox="0 0 36 28"><path d="M2 28V16C2 7 7 2 15 0v5c-4 2-6 5-6 9h6v14zM21 28V16c0-9 5-14 13-16v5c-4 2-6 5-6 9h6v14z" fill="#fff"/></svg>
  <p class="quote">Our systems have never been more secure. The team worked alongside our staff from the first day, answered every question and delivered a clear plan that we still follow today.</p>
  <div class="avatar"></div>
  <div class="person">Person Name<small>Client Director</small></div>
</section>

<section class="partners">
  <div class="partner"><i></i>ChatShield</div>
  <div class="partner"><i></i>FlareSight</div>
  <div class="partner"><i></i>LogCadence</div>
  <div class="partner"><i></i>CipherVault</div>
  <div class="partner"><i></i>Sentrix</div>
</section>

<footer class="footer">
  <span>Home/About Us/Service/Careers/contacts/contact Us</span>
  <span>© 2014-2015 V9 Group All rights Reserved</span>
</footer>

</body>
</html>
```